Counselling practice needs a Business Card Design

I need a business card design for a new counselling practice in Canberra, Australia. The name of the practice is Dr Glen Hartwick, Counselling Services and the practice focuses on philosophical, narrative and existential counselling for individuals, couples and families. The final design should communicate professionalism, sophistication of analysis and psychological wholeness. The reverse side of the card should have an appointment reminder

Could the following qualifications also be included on card. BSc (Psychology), BA hons (Philosophy), PhD (Philosophy), Diploma of Community Counselling And the following affiliation Guild of Talk Therapists for the Southern Tablelands Inc. (GOTTST) And my contact phone mobile phone number is 0497385164, and email is Glen.Hartwick274@mailvesta.example for inclusion as well.

Thank you all who have put in a design so far. I just wanted to clarify some design points based on what you have submitted. 1. The Guild of Talk Therapists. Southern Tablelands Inc. (GOTTST) is an affiliation only. 'Member of the Guild of Talk Therapists. Southern Tablelands Inc (GOTTST)' should appear with the same prominence of a qualification. 2. The Post Graduate Diploma in Community Counselling is a quaification and should appear as 'PG Dip (Community Counselling)' after the other qualifications. 3. I am advertising myself as a counsellor so 'Dr Glen Hartwick, Counselling Services' or 'Dr Glen Hartwick, Counsellor' is the equivalent of the business name. After looking at some of the designs I prefer Dr Glen Hartwick in sentence case rather than all capitals (DR GLEN HARTWICK). 4. 'Philosophical, narrative and existential counselling for individuals, couples and families' is the description of the type of counselling services and should appear on the card.

One further point. I have updated my email address for the card. It is now drglenhartwick@quietharbourtherapy.example

```html
<!DOCTYPE html>
<html lang="en">
<head>
<meta charset="utf-8">
<title>Dr Glen Hartwick, Counselling Services – Business Card</title>
<link rel="stylesheet" href="https://fonts.googleapis.com/css2?family=Arimo:wght@400;700&display=swap">
<style>
  :root {
    --stage: #e9e6e1;
    --ink: #111111;
    --paper: #ffffff;
    --card-black: #0b0b0b;
    --frame-grey: #6b6b6b;
    --rule-light: #d8d8d8;
    --rule-dark: #222222;
    --text-soft: #2a2a2a;
  }
  * { box-sizing: border-box; margin: 0; padding: 0; }
  html, body {
    width: 1200px; height: 1000px; overflow: hidden;
    background: var(--stage);
    font-family: "Arimo", Arial, sans-serif;
    color: var(--ink);
  }
  .canvas {
    width: 1200px; height: 1000px;
    display: flex; flex-direction: column;
    align-items: center; justify-content: center;
    gap: 40px;
  }
  .card {
    width: 770px; height: 440px;
    border-radius: 34px;
    position: relative;
    overflow: hidden;
    box-shadow: 0 6px 18px rgba(0,0,0,0.18);
  }

  /* Back: affiliation side */
  .card--back { background: var(--card-black); color: var(--paper); }
  .card--back .inner-frame {
    position: absolute; inset: 16px;
    border: 2px solid var(--frame-grey);
    border-radius: 22px;
  }
  .affiliation {
    position: absolute; left: 120px; top: 120px; width: 540px;
  }
  .affiliation__acronym {
    font-weight: 700; font-size: 92px; letter-spacing: 2px;
    line-height: 1; padding-bottom: 10px;
  }
  .affiliation__rule {
    height: 2px; background: var(--rule-light); width: 100%;
  }
  .affiliation__text {
    margin-top: 12px;
    font-size: 22px; line-height: 1.25; color: var(--rule-light);
  }

  /* Front: practitioner side */
  .card--front { background: var(--paper); }
  .front__top {
    position: absolute; left: 70px; top: 58px; right: 60px;
    display: flex; align-items: flex-start;
  }
  .identity { display: flex; flex-direction: column; align-items: flex-end; }
  .identity__name { font-weight: 700; font-size: 40px; line-height: 1.05; }
  .identity__role { font-size: 22px; margin-top: 4px; }
  .front__divider {
    width: 2px; height: 140px; background: var(--rule-dark);
    margin: 50px 28px 0 60px;
  }
  .contact { margin-top: 108px; font-size: 22px; line-height: 1.45; }
  .contact__line { display: flex; align-items: center; gap: 8px; white-space: nowrap; }
  .contact__icon { width: 18px; height: 18px; flex: none; }

  .front__bottom {
    position: absolute; left: 70px; right: 50px; bottom: 50px;
    color: var(--text-soft);
  }
  .qualifications { font-size: 21px; margin-bottom: 6px; }
  .qualifications strong { font-weight: 700; color: var(--ink); }
  .description { font-size: 19.5px; line-height: 1.3; }
</style>
</head>
<body>
<main class="canvas">

  <section class="card card--back" aria-label="Card back, affiliation">
    <div class="inner-frame"></div>
    <div class="affiliation">
      <div class="affiliation__acronym">GOTTST</div>
      <div class="affiliation__rule"></div>
      <p class="affiliation__text">Diploma of Community Counselling And the following affiliation Guild of Talk Therapists for the Southern Tablelands Inc.</p>
    </div>
  </section>

  <section class="card card--front" aria-label="Card front, practitioner details">
    <div class="front__top">
      <div class="identity">
        <h1 class="identity__name">Dr Glen Hartwick</h1>
        <p class="identity__role">Counselling Services</p>
      </div>
      <div class="front__divider"></div>
      <div class="contact">
        <p class="contact__line">
          <svg class="contact__icon" viewBox="0 0 24 24" aria-hidden="true"><path fill="#111" d="M6.6 10.8a15.1 15.1 0 0 0 6.6 6.6l2.2-2.2c.3-.3.7-.4 1-.2 1.1.4 2.3.6 3.6.6.6 0 1 .4 1 1V20c0 .6-.4 1-1 1A17 17 0 0 1 3 4c0-.6.4-1 1-1h3.5c.6 0 1 .4 1 1 0 1.3.2 2.5.6 3.6.1.3 0 .7-.2 1z"/></svg>
          04.97.38.5164
        </p>
        <p class="contact__line">
          <svg class="contact__icon" viewBox="0 0 24 24" aria-hidden="true"><rect x="2" y="5" width="20" height="14" rx="1.5" fill="#111"/><path d="M3 6.5l9 6.5 9-6.5" fill="none" stroke="#fff" stroke-width="1.8"/></svg>
          Glen.Hartwick274@mailvesta.example
        </p>
      </div>
    </div>

    <div class="front__bottom">
      <p class="qualifications"><strong>BSc</strong> (Psychology) &bull; <strong>BA hons</strong> (Philosophy) &bull; <strong>PhD</strong> (Philosophy)</p>
      <p class="description">Counselling Services and the practice focuses on philosophical narrative and existential counselling for individuals, couples and families.</p>
    </div>
  </section>

</main>
</body>
</html>
```